Business Card Design Project

I require a business card for a new coaching business based in Melbourne with global clients. Both companies and individuals will retain our coaching services.

Target Market(s)

Both small business and large corporate in western speaking countries. Individuals requiring support and direction on issues such as fears, phobias, career, relationships, confidence, self esteem etc.

Industry/Entity Type

Business

Font styles to use
Sans Serif

Colors

Designer to choose colors to be used in the design.

Requirements
Must have
• White background to enhance the colours in the logo. Logo on the left.
Should not have
• The black and white version of the logo. Keep the colours.

```html
<!DOCTYPE html>
<html lang="en">
<head>
<meta charset="utf-8">
<title>Clear Path Coaching – Business Card</title>
<link href="https://fonts.googleapis.com/css2?family=Open+Sans:wght@400;700&display=swap" rel="stylesheet">
<style>
  :root {
    --backdrop: #e7e4df;
    --card: #ffffff;
    --ink: #4a4a4a;
    --ink-soft: #5c5c5c;
    --name-blue: #1a8fe3;
    --pink: #ff0a7e;
    --orange: #ff7a00;
    --green: #66de00;
    --blue: #0a84ff;
    --rule: #d4d4d4;
  }
  * { margin: 0; padding: 0; box-sizing: border-box; }
  html, body {
    width: 1200px;
    height: 1045px;
    overflow: hidden;
    background: var(--backdrop);
    font-family: "Open Sans", Arial, sans-serif;
  }
  .canvas { position: relative; width: 1200px; height: 1045px; }

  .card {
    position: absolute;
    left: 258px;
    width: 697px;
    height: 400px;
    background: var(--card);
    box-shadow: 0 4px 14px rgba(0,0,0,0.18);
    overflow: hidden;
  }
  .card--front { top: 80px; }
  .card--back { top: 521px; }

  .colour-band {
    position: absolute;
    left: 0; right: 0; bottom: 0;
    height: 8px;
    display: flex;
  }
  .colour-band span { flex: 1; }
  .colour-band .pink { background: var(--pink); }
  .colour-band .orange { background: var(--orange); }
  .colour-band .green { background: var(--green); }
  .colour-band .blue { background: var(--blue); }

  .brand {
    position: absolute;
    display: flex;
    align-items: center;
    gap: 16px;
  }
  .brand__dot {
    flex: none;
    border-radius: 50%;
    background: var(--pink);
  }
  .brand__name {
    font-weight: 700;
    text-transform: uppercase;
    line-height: 1.05;
    letter-spacing: 0.5px;
    color: var(--ink);
    white-space: nowrap;
  }
  .card--front .brand { left: 60px; top: 174px; }
  .card--front .brand__dot { width: 72px; height: 72px; }
  .card--front .brand__name { font-size: 25px; }

  .card--back .brand { left: 178px; top: 150px; }
  .card--back .brand__dot { width: 100px; height: 100px; }
  .card--back .brand__name { font-size: 34px; }

  .divider {
    position: absolute;
    left: 346px;
    top: 146px;
    width: 1px;
    height: 131px;
    background: var(--rule);
  }

  .contact {
    position: absolute;
    left: 373px;
    top: 137px;
  }
  .contact__name {
    font-size: 20px;
    font-weight: 700;
    color: var(--name-blue);
    line-height: 1.3;
  }
  .contact__role {
    font-size: 15px;
    color: var(--ink-soft);
    margin-top: 2px;
  }
  .contact__list {
    list-style: none;
    margin-top: 18px;
    font-size: 15px;
    color: var(--ink-soft);
    line-height: 25px;
  }
  .contact__label { font-weight: 700; margin-right: 3px; }
  .contact__label--t { color: var(--pink); }
  .contact__label--f { color: var(--green); }
  .contact__label--e { color: var(--orange); }
</style>
</head>
<body>
<main class="canvas">
  <section class="card card--front">
    <div class="brand">
      <span class="brand__dot"></span>
      <span class="brand__name">Clear Path<br>Coaching</span>
    </div>
    <div class="divider"></div>
    <div class="contact">
      <h1 class="contact__name">Maren Holloway-Price</h1>
      <p class="contact__role">Performance Consultant and Coach</p>
      <ul class="contact__list">
        <li><span class="contact__label contact__label--t">T:</span>+61 (0) 400 555 120</li>
        <li><span class="contact__label contact__label--f">F:</span>+61 (0) 400 555 120</li>
        <li><span class="contact__label contact__label--e">E:</span>maren@clearpathcoaching.com</li>
      </ul>
    </div>
    <div class="colour-band"><span class="pink"></span><span class="orange"></span><span class="green"></span><span class="blue"></span></div>
  </section>

  <section class="card card--back">
    <div class="brand">
      <span class="brand__dot"></span>
      <span class="brand__name">Clear Path<br>Coaching</span>
    </div>
    <div class="colour-band"><span class="pink"></span><span class="orange"></span><span class="green"></span><span class="blue"></span></div>
  </section>
</main>
</body>
</html>
```